2022 Copper Gull Classic poster

Event poster for the 35th annual sailboat race from Galveston to Port Aransas. [will upgrade to guaranteed once a couple of serious designs are submitted] Hosted by Brinehaven Yacht Club in Seabrook TX, organized by Tern Ridge Sailing Foundation, a charity supporting youth sailing and amateur sailboat racing. The poster art (or elements of it) will also be used for T shirts. This year's theme is "Marigold Evenings" in honor of 35 years of sponsorship by Corvello Rum. Past posters normally include a full moon (usually orange) and a sailboat or numerous sailing yachts 30 foot and up. This year we would like to add the Cuban party theme. About 1/4 of the poster space (usually at the bottom) will focus on event sponsors. Brinehaven Yacht Club or its burgee should be included but it is a minor element.

Target Market(s)

adult racing and cruising sailors and sailing yacht owners in the Gulf of Mexico vacinity who like to race overnight to a big party

Industry/Entity Type

adult sailboat distance offshore racing

Requirements
Must have
• 30' or larger sailboat(s), full moon (often orange but not absolute requirement), Copper Gull Classic® with the registered trade mark symbol, date (Oct 6-8, 2022), reference to Brinehaven Yacht Club either in text or by including the burgee with BYC and a seahorse... see uploaded options, [much of the must haves could be addressed by including the registered trademark logo with 2022 included, maybe as one element of an art nouveau style poster... see Love the feel uploaded example]
Nice to have
• see uploaded "love the feel of this" for one idea on how to incorporate dirent must haves with nice to haves; reference to 35 or 35th annual, Marigold Evenings Party feel, Rum reference or Corvello Rum reference (bat logo, liquor bottle with "Rum" or generic cocktail in the hand of a partier, tropical party influence (like salsa dancing couple or steel drum band)
Should not have
• reference to any brand of alcohol other than Corvello rum (no Martini glass, no beer stein)

```html
<!DOCTYPE html>
<html lang="en">
<head>
<meta charset="utf-8">
<title>Copper Gull Classic 2022 – Poster</title>
<link href="https://fonts.googleapis.com/css2?family=Anton&family=Oswald:wght@200;300;600&family=Questrial&family=Jura:wght@300&display=swap" rel="stylesheet">
<style>
  :root {
    --navy: #14305a;
    --cream: #ece5c3;
    --khaki: #d6cf96;
    --night: #1c1a45;
    --deep-blue: #0f4b78;
    --dusk: #8a6178;
    --glow: #f2b57a;
    --backdrop: #161616;
  }
  html, body {
    margin: 0;
    width: 907px;
    height: 1200px;
    overflow: hidden;
    background: var(--backdrop);
  }
  .poster {
    position: absolute;
    left: 29px;
    top: 0;
    width: 849px;
    height: 1200px;
    background: var(--cream);
    overflow: hidden;
    font-family: "Questrial", sans-serif;
  }
  .scene {
    position: absolute;
    left: 0;
    top: 0;
    width: 557px;
    height: 1000px;
    background:
      radial-gradient(ellipse 210px 150px at 14% 82%, var(--glow) 0%, rgba(242,181,122,0.55) 45%, rgba(242,181,122,0) 100%),
      linear-gradient(180deg, var(--night) 0%, #1a2a5a 35%, var(--deep-blue) 62%, var(--dusk) 80%, #4f6b78 88%, #6a5a4a 100%);
  }
  .display {
    position: absolute;
    left: 0;
    top: 0;
    width: 849px;
    height: 1200px;
  }
  .display .heavy { font-family: "Anton", sans-serif; }
  .display .thin-condensed { font-family: "Oswald", sans-serif; font-weight: 300; }
  .display .thin-wide { font-family: "Questrial", sans-serif; }
  .display .thin-square { font-family: "Jura", sans-serif; font-weight: 300; }

  .route {
    position: absolute;
    left: 33px;
    top: 262px;
    width: 404px;
    height: 27px;
    border: 1px solid var(--cream);
    color: var(--cream);
    font-size: 21px;
    line-height: 27px;
    text-align: center;
    white-space: nowrap;
    letter-spacing: 0.3px;
  }
  .organizer {
    position: absolute;
    left: 260px;
    top: 303px;
    width: 179px;
    height: 151px;
  }
  .organizer-label {
    height: 39px;
    background: var(--cream);
    color: var(--navy);
    font-family: "Anton", sans-serif;
    font-size: 22px;
    line-height: 39px;
    text-align: center;
    letter-spacing: 0.5px;
  }
  .organizer-name {
    box-sizing: border-box;
    height: 112px;
    border: 1px solid var(--cream);
    border-top: none;
    color: var(--cream);
    font-family: "Oswald", sans-serif;
    font-weight: 200;
    font-size: 31px;
    line-height: 35px;
    padding: 4px 0 0 9px;
    white-space: nowrap;
  }
  .partners {
    position: absolute;
    left: 0;
    top: 859px;
    width: 333px;
    height: 141px;
    background: var(--cream);
  }
  .partner {
    position: absolute;
    top: 7px;
    height: 120px;
    box-sizing: border-box;
    border: 1px solid var(--navy);
    text-align: center;
    color: var(--navy);
  }
  .partner.host { left: 26px; width: 126px; }
  .partner.sponsor { left: 172px; width: 147px; }
  .partner-label {
    height: 39px;
    background: var(--navy);
    color: var(--cream);
    font-family: "Anton", sans-serif;
    font-size: 25px;
    line-height: 39px;
    white-space: nowrap;
  }
  .partner.sponsor .partner-label { font-size: 20px; }
  .partner-mark {
    width: 22px;
    height: 22px;
    margin: 12px auto 8px;
    background: var(--navy);
  }
  .partner-mark.round { border-radius: 50%; width: 28px; height: 28px; margin: 10px auto 6px; }
  .partner-name {
    font-family: "Oswald", sans-serif;
    font-weight: 600;
    font-size: 10px;
    line-height: 13px;
    letter-spacing: 0.2px;
  }
  .partner.sponsor .partner-name {
    font-size: 21px;
    line-height: 26px;
    letter-spacing: 1px;
  }
  .audience {
    position: absolute;
    left: 583px;
    top: 1011px;
    width: 243px;
  }
  .audience-row {
    box-sizing: border-box;
    border: 1px solid var(--navy);
    color: var(--navy);
    white-space: nowrap;
  }
  .audience-row.lead {
    height: 41px;
    background: var(--navy);
    color: var(--cream);
    font-size: 26px;
    line-height: 41px;
    text-align: center;
  }
  .audience-row.second {
    height: 38px;
    border-top: none;
    font-size: 22px;
    line-height: 36px;
    text-align: center;
  }
  .audience-row.third {
    height: 89px;
    border-top: none;
    font-size: 17.5px;
    line-height: 20px;
    padding: 9px 0 0 10px;
  }
</style>
</head>
<body>
<main class="poster">
  <div class="scene" role="img" aria-label="Night sky illustration with stars, a large orange full moon on the horizon, a dark sailboat silhouette carrying the event badge on its mainsail, a second sailboat, calm water and a wooden dock"></div>

  <svg class="display" viewBox="0 0 849 1200" xmlns="http://www.w3.org/2000/svg">
    <g class="heavy" fill="var(--cream)">
      <text x="31" y="178" font-size="144" textLength="154" lengthAdjust="spacingAndGlyphs">35</text>
      <text x="193" y="81" font-size="44" textLength="43" lengthAdjust="spacingAndGlyphs">th</text>
      <text x="193" y="160" font-size="67" textLength="248" lengthAdjust="spacingAndGlyphs">ANNUAL</text>
      <text x="35" y="250" font-size="93" textLength="405" lengthAdjust="spacingAndGlyphs">SAILBOAT RACE</text>
      <text x="31" y="454" font-size="126" textLength="218" lengthAdjust="spacingAndGlyphs">2022</text>
    </g>
    <text class="thin-condensed" x="31" y="339" font-size="42" fill="var(--cream)" textLength="218" lengthAdjust="spacingAndGlyphs">6<tspan font-size="21" dy="-16">th</tspan><tspan dy="16"> - 8</tspan><tspan font-size="21" dy="-16">th</tspan><tspan dy="16"> OCTOBER</tspan></text>

    <text class="heavy" transform="translate(687 983) rotate(-90)" x="0" y="0" font-size="126" fill="var(--navy)" textLength="922" lengthAdjust="spacingAndGlyphs">COPPER GULL CLASSIC</text>
    <text class="thin-wide" transform="translate(604 62) rotate(-90)" x="0" y="0" font-size="30" fill="var(--navy)">®</text>

    <rect x="714.5" y="52.5" width="110" height="934" fill="var(--khaki)" stroke="var(--navy)" stroke-width="1"/>
    <text class="thin-square" transform="translate(807 966) rotate(-90)" x="0" y="0" font-size="108" fill="var(--navy)" textLength="895" lengthAdjust="spacingAndGlyphs">SAILBOAT RACE</text>

    <text class="thin-wide" x="22" y="1051" font-size="66" fill="var(--navy)" textLength="533" lengthAdjust="spacingAndGlyphs">RACE OVERNIGHT</text>
    <rect x="22" y="1065" width="535" height="109" fill="var(--navy)"/>
    <text class="heavy" x="28" y="1168" font-size="114" fill="var(--cream)" textLength="519" lengthAdjust="spacingAndGlyphs">TO A BIG PARTY</text>
  </svg>

  <div class="route">GALVESTON TO PORT ARANSAS</div>

  <div class="organizer">
    <div class="organizer-label">ORGANIZED BY</div>
    <div class="organizer-name">TERN RIDGE<br>SAILING<br>FOUNDATION</div>
  </div>

  <section class="partners">
    <div class="partner host">
      <div class="partner-label">HOSTED BY</div>
      <div class="partner-mark"></div>
      <div class="partner-name">BRINEHAVEN YACHT CLUB<br>IN SEABROOK TX</div>
    </div>
    <div class="partner sponsor">
      <div class="partner-label">SPONSORSHIP BY</div>
      <div class="partner-mark round"></div>
      <div class="partner-name">CORVELLO</div>
    </div>
  </section>

  <section class="audience">
    <div class="audience-row lead">ADULT RACING</div>
    <div class="audience-row second">CRUISING SAILORS</div>
    <div class="audience-row third">SAILING YACHT OWNERS<br>IN THE GULF OF MEXICO<br>VACINITY</div>
  </section>
</main>
</body>
</html>
```